Letterhead & Email Signature Design

Kindly assist redesign this letterhead as well as the Email signature. I have uploaded the current designs that needs some new look

```html
<!DOCTYPE html>
<html lang="en">
<head>
<meta charset="utf-8">
<title>Moyo Dlamini Inc — Stationery</title>
<link rel="stylesheet" href="https://fonts.googleapis.com/css2?family=Montserrat:wght@800&family=Poppins:wght@400&display=swap">
<style>
  :root {
    --backdrop: #ebebeb;
    --paper: #ffffff;
    --ink: #111111;
    --edge: #3a3a3a;
    --text: #222222;
  }
  * { margin: 0; padding: 0; box-sizing: border-box; }
  html, body { width: 1200px; height: 1085px; overflow: hidden; background: var(--backdrop); }
  .stage { position: relative; width: 1200px; height: 1085px; }

  .letterhead {
    position: absolute; left: 414px; top: 98px; width: 677px; height: 874px;
    background: var(--paper); border: 1px solid var(--edge); overflow: hidden;
  }
  .letterhead .band { position: absolute; left: 0; top: 0; }
  .letterhead .brand-name {
    position: absolute; left: 27px; top: 38px; width: 100px; text-align: center;
    font: 800 10px/1.15 "Montserrat", sans-serif; color: var(--ink); letter-spacing: 0.5px;
  }
  .letterhead .footer {
    position: absolute; left: 0; top: 840px; width: 100%; height: 18px;
    font: 400 11px/18px "Poppins", sans-serif; color: var(--text);
  }
  .footer .item { position: absolute; display: flex; align-items: center; gap: 6px; }

  .business-card {
    position: absolute; left: 116px; top: 419px; width: 665px; height: 354px;
    background: var(--paper); border: 1px solid var(--edge); overflow: hidden; z-index: 2;
  }
  .business-card .band { position: absolute; left: 0; top: 0; }
  .business-card .brand-name {
    position: absolute; left: 236px; top: 146px; width: 190px; text-align: center;
    font: 800 17px/1.2 "Montserrat", sans-serif; color: var(--ink); letter-spacing: 1px;
  }
  .holder { position: absolute; left: 41px; top: 53px; width: 190px; text-align: center; }
  .holder .name { font: 800 17px/1 "Montserrat", sans-serif; color: var(--ink); letter-spacing: 1.5px; }
  .holder .role { margin-top: 6px; font: 400 11px/1 "Poppins", sans-serif; letter-spacing: 7px; color: var(--text); }
  .firm { position: absolute; left: 41px; top: 154px; width: 190px; text-align: center; }
  .firm .line { font: 800 17px/1.1 "Montserrat", sans-serif; color: var(--ink); letter-spacing: 1.5px; }
  .firm .est { margin-top: 1px; font: 400 12px/1 "Poppins", sans-serif; letter-spacing: 1px; color: var(--text); }

  .contacts { position: absolute; left: 461px; top: 53px; font: 400 11px/15px "Poppins", sans-serif; color: var(--text); }
  .contacts .row { position: absolute; left: 0; display: flex; gap: 6px; white-space: nowrap; }
  .icon { width: 12px; height: 12px; flex: none; margin-top: 1px; }
</style>
</head>
<body>
<svg width="0" height="0" style="position:absolute">
  <defs>
    <symbol id="icon-pin" viewBox="0 0 12 12"><circle cx="6" cy="6" r="6" fill="#111"/><path d="M6 2.5a2 2 0 0 0-2 2c0 1.6 2 4 2 4s2-2.4 2-4a2 2 0 0 0-2-2z" fill="#fff"/><circle cx="6" cy="4.5" r=".7" fill="#111"/></symbol>
    <symbol id="icon-phone" viewBox="0 0 12 12"><circle cx="6" cy="6" r="6" fill="#111"/><path d="M4 3l1.2 1.4-.6.8c.4.9 1.1 1.6 2 2l.8-.6L9 8l-.7 1C6 9 3 6 3 3.7z" fill="#fff"/></symbol>
    <symbol id="icon-mail" viewBox="0 0 12 12"><circle cx="6" cy="6" r="6" fill="#111"/><rect x="3" y="4" width="6" height="4.2" fill="#fff"/><path d="M3 4l3 2.3L9 4" stroke="#111" stroke-width=".7" fill="none"/></symbol>
    <symbol id="icon-web" viewBox="0 0 12 12"><circle cx="6" cy="6" r="6" fill="#111"/><circle cx="6" cy="6" r="3" fill="none" stroke="#fff" stroke-width=".8"/><path d="M3 6h6M6 3v6" stroke="#fff" stroke-width=".7"/></symbol>
  </defs>
</svg>

<main class="stage">
  <section class="letterhead" aria-label="Letterhead">
    <svg class="band" width="160" height="490" viewBox="0 0 160 490">
      <polygon points="76,0 125,0 0,480 0,292" fill="var(--ink)"/>
      <ellipse cx="77" cy="54" rx="60" ry="42" fill="var(--paper)"/>
    </svg>
    <div class="brand-name">MOYO<br>DLAMINI INC</div>
    <footer class="footer">
      <span class="item" style="left:45px"><svg class="icon"><use href="#icon-phone"/></svg>+27 11 555 0148</span>
      <span class="item" style="left:216px"><svg class="icon"><use href="#icon-mail"/></svg>Naledi@moyodlamini.co.za</span>
      <span class="item" style="left:462px"><svg class="icon"><use href="#icon-web"/></svg>www.moyodlaminiinc.co.za</span>
    </footer>
  </section>

  <section class="business-card" aria-label="Business card">
    <svg class="band" width="665" height="354" viewBox="0 0 665 354">
      <polygon points="364,0 444,0 298,354 223,354" fill="var(--ink)"/>
      <ellipse cx="331" cy="169" rx="116" ry="86" fill="var(--paper)"/>
    </svg>
    <div class="brand-name">MOYO<br>DLAMINI INC</div>

    <div class="holder">
      <div class="name">NALEDI SITHOLE</div>
      <div class="role">DIRECTOR</div>
    </div>
    <div class="firm">
      <div class="line">DLAMINI INC</div>
      <div class="line">MOYO</div>
      <div class="est">EST. 2009</div>
    </div>

    <div class="contacts">
      <div class="row" style="top:0"><svg class="icon"><use href="#icon-pin"/></svg><span>214 Acacia Road,<br>The Meadows</span></div>
      <div class="row" style="top:44px"><svg class="icon"><use href="#icon-pin"/></svg><span>Office Park, Ground Floor,<br>Building B, 48 Marula Street,<br>Oak Park, Riverton</span></div>
      <div class="row" style="top:104px"><svg class="icon"><use href="#icon-phone"/></svg><span>+27 11 555 0148</span></div>
      <div class="row" style="top:120px"><svg class="icon"><use href="#icon-mail"/></svg><span>Naledi@moyodlamini.co.za</span></div>
      <div class="row" style="top:136px"><svg class="icon"><use href="#icon-web"/></svg><span>www.moyodlaminiinc.co.za</span></div>
    </div>
  </section>
</main>
</body>
</html>
```